Tess Marlowe Communication business card

I am starting a small, country-based business that offers writing, communication and marketing services to a wide range of clients, inner city big business, to mining, through to agriculture.

The appeal of my business is that it's mobile and flexible. It's just me, with lots of hands-on experience on construction and infrastructure projects.

I can provide the following services:

• Communication planning and management
• Issues and media management
• Marketing and communication materials
• Project management and strategy
• Government liaison
• Incident management communication
• Stakeholder management

It would be great to be able to use the elements of the business card design on other stationery.

Industry/Entity Type

Communication

Requirements
Must have
• The following information:

Tess Marlowe
M: 0427 391 864
E: tess@tmcommsmail.com

PO Box 152
Durrandale Q 4472
Nice to have
• a rural element (windmill, workboots, wheat stalk)

```html
<!DOCTYPE html>
<html lang="en">
<head>
<meta charset="utf-8">
<title>Tess Marlowe Communication – Business Card</title>
<link rel="stylesheet" href="https://fonts.googleapis.com/css2?family=Arimo&family=Comfortaa:wght@600;700&display=swap">
<style>
  :root {
    --card-black: #000000;
    --ink-white: #ffffff;
    --edge-blue: #0a3f95;
  }
  html, body {
    margin: 0;
    padding: 0;
    width: 1200px;
    height: 686px;
    overflow: hidden;
    background: var(--card-black);
  }
  .card {
    position: relative;
    width: 1200px;
    height: 686px;
    background: var(--card-black);
    color: var(--ink-white);
    overflow: hidden;
  }
  .edge-band {
    position: absolute;
    top: 0;
    right: 0;
    width: 32px;
    height: 686px;
    background: var(--edge-blue);
  }
  .brand-name {
    position: absolute;
    top: 52px;
    right: 56px;
    margin: 0;
    font-family: "Comfortaa", sans-serif;
    font-weight: 700;
    font-size: 48px;
    letter-spacing: -0.5px;
    line-height: 1;
    white-space: nowrap;
    text-transform: lowercase;
  }
  .services {
    position: absolute;
    left: 600px;
    top: 268px;
    margin: 0;
    padding: 0;
    list-style: none;
    font-family: "Comfortaa", sans-serif;
    font-weight: 600;
    font-size: 34px;
    letter-spacing: -0.5px;
    line-height: 1.1;
  }
  .services li {
    position: relative;
    padding-left: 32px;
    margin-bottom: 25px;
  }
  .services li::before {
    content: "";
    position: absolute;
    left: 6px;
    top: 16px;
    width: 9px;
    height: 9px;
    border-radius: 50%;
    background: var(--ink-white);
  }
  .services li.two-line {
    padding-left: 32px;
  }
  .services li.two-line span {
    display: block;
    padding-left: 26px;
    margin-top: 8px;
  }
  .contact {
    position: absolute;
    left: 0;
    width: 594px;
    top: 422px;
    margin: 0;
    font-family: "Arimo", Arial, sans-serif;
    font-style: normal;
    font-size: 37px;
    line-height: 51.5px;
    text-align: center;
  }
  .contact p {
    margin: 0;
    white-space: nowrap;
  }
</style>
</head>
<body>
  <main class="card">
    <h1 class="brand-name">tess marlowe communication</h1>

    <ul class="services">
      <li>stakeholder management</li>
      <li>government liaison</li>
      <li class="two-line">issues and media<span>management</span></li>
    </ul>

    <address class="contact">
      <p class="contact-name">Tess Marlowe</p>
      <p class="contact-mobile">M: 0427 391 864</p>
      <p class="contact-box">PO Box 152</p>
      <p class="contact-town">Durrandale Q 4472</p>
      <p class="contact-email">E: tess@tmcommsmail.com</p>
    </address>

    <div class="edge-band"></div>
  </main>
</body>
</html>
```